Will you marry me post card

I am just looking for a postcard to send my partner that will ask him to marry me.
I plan on creating about 200 of them and mailing them all at once so that he gets them all on the same day.
They should all be similar or could have a few different options.
I would like it simple, elegant, clean and crisp. No images, just text or icons

My only requirement is the text, "will you marry me?" in all lowercase -- any fonts, can be big, small, varying sizes, repeated, whole card, tiny space, don't care...just amazing design. BUT SIMPLE!

```html
<!DOCTYPE html>
<html lang="en">
<head>
<meta charset="utf-8">
<title>will you marry me? — postcard</title>
<link rel="stylesheet" href="https://fonts.googleapis.com/css2?family=Crimson+Pro:wght@500&display=swap">
<style>
  :root {
    --page-black: #000000;
    --satin-dark: #19191b;
    --satin-mid: #2b2b2e;
    --glitter-gold: #5e400e;
    --glitter-glow: #7d5413;
    --headline-white: #ffffff;
    --headline-shadow: rgba(0, 0, 0, 0.85);
  }

  html, body {
    margin: 0;
    padding: 0;
    width: 1200px;
    height: 1000px;
    overflow: hidden;
    background: var(--page-black);
  }

  .canvas {
    position: relative;
    width: 1200px;
    height: 1000px;
    background: var(--page-black);
  }

  .postcard {
    position: absolute;
    left: 182px;
    top: 176px;
    width: 836px;
    height: 648px;
    overflow: hidden;
  }

  .postcard__backdrop {
    position: absolute;
    inset: 0;
    background: linear-gradient(178deg,
      var(--satin-mid) 0%,
      var(--satin-dark) 25%,
      var(--glitter-gold) 40%,
      var(--glitter-glow) 50%,
      var(--glitter-gold) 62%,
      var(--satin-dark) 78%,
      var(--satin-mid) 100%);
  }

  .postcard__headline {
    position: absolute;
    left: 0;
    right: 0;
    top: 262px;
    margin: 0;
    text-align: center;
    font-family: "Crimson Pro", "Palatino Linotype", Georgia, serif;
    font-weight: 500;
    font-size: 92px;
    line-height: 1;
    letter-spacing: 1px;
    color: var(--headline-white);
    text-shadow: 3px 5px 4px var(--headline-shadow), 0 0 2px var(--headline-shadow);
  }
</style>
</head>
<body>
  <main class="canvas">
    <section class="postcard">
      <div class="postcard__backdrop" role="img" aria-label="Dark black satin folds with a sweeping band of sparkling gold glitter and bokeh across the middle"></div>
      <h1 class="postcard__headline">will you marry me?</h1>
    </section>
  </main>
</body>
</html>
```